Private Medical Clinic needs a letterhead design

Letterhead that can be edited. Letter head is needed for printing official doctor's notes, referrals, etc in a medical clinic. The letterhead should use the attached logos

```html
<!DOCTYPE html>
<html lang="en">
<head>
<meta charset="utf-8">
<title>Cedar Hollow Family Medicine – Letterhead</title>
<link href="https://fonts.googleapis.com/css2?family=Arimo:wght@400;700&family=Damion&display=swap" rel="stylesheet">
<style>
  :root {
    --backdrop: #ececec;
    --paper: #f7f7f7;
    --ink: #1e1e1e;
    --ink-soft: #555555;
    --brand-green: #3e6a3c;
    --brand-green-light: #ffffff;
    --decor-tone: #dedede;
  }
  * { margin: 0; padding: 0; box-sizing: border-box; }
  html, body {
    width: 1200px; height: 795px; overflow: hidden;
    background: var(--backdrop);
    font-family: "Arimo", Arial, sans-serif;
    color: var(--ink);
  }
  .canvas {
    width: 1200px; height: 795px;
    display: flex; align-items: center; justify-content: center;
  }
  .letterhead {
    position: relative;
    width: 530px; height: 750px;
    background: var(--paper);
    box-shadow: 0 2px 10px rgba(0,0,0,0.12);
    overflow: hidden;
  }
  .brand {
    position: absolute; top: 70px; left: 0; right: 0;
    display: flex; align-items: center; justify-content: center; gap: 8px;
  }
  .brand-dot {
    width: 14px; height: 14px; border-radius: 50%;
    background: var(--ink-soft);
  }
  .brand-name {
    font-size: 18px; font-weight: 400; color: var(--ink-soft);
    letter-spacing: 0.5px;
  }
  .recipient {
    position: absolute; top: 215px; left: 52px;
    font-size: 9.5px; line-height: 1.3;
  }
  .recipient-name { font-weight: 700; font-size: 10.5px; }
  .letter-body {
    position: absolute; top: 275px; left: 52px; width: 426px;
    font-size: 9.6px; line-height: 1.55;
  }
  .letter-body p { margin-bottom: 14px; }
  .decor-bloom {
    position: absolute; left: 120px; top: 470px;
    width: 240px; height: 250px;
    border-radius: 50% 50% 10% 10%;
    background: radial-gradient(circle at 45% 40%, var(--decor-tone) 0%, rgba(222,222,222,0.45) 45%, rgba(247,247,247,0) 72%);
  }
  .signoff {
    position: absolute; top: 535px; left: 52px;
    font-size: 9.6px;
  }
  .signature {
    position: absolute; top: 560px; left: 60px;
    font-family: "Damion", cursive;
    font-size: 40px; color: var(--ink);
  }
  .signer {
    position: absolute; top: 612px; left: 76px;
    font-size: 10px; line-height: 1.3;
  }
  .signer-title { font-weight: 700; }
  .contact {
    position: absolute; right: 30px; top: 640px;
    text-align: right; font-size: 8.4px; line-height: 1.5; color: var(--ink);
  }
  .contact-company { font-weight: 700; font-size: 9.6px; }
  .contact strong { font-weight: 700; }
  .contact-email { color: var(--ink-soft); }
  .footer-band {
    position: absolute; left: 0; right: 0; bottom: 0; height: 4px;
    background: var(--brand-green);
  }
  .footer-tab {
    position: absolute; right: 0; bottom: 0;
    width: 290px; height: 24px;
    background: var(--brand-green);
    border-top-left-radius: 12px;
    display: flex; align-items: center; justify-content: center;
    color: var(--brand-green-light);
    font-size: 8.5px; letter-spacing: 4px;
  }
</style>
</head>
<body>
<main class="canvas">
  <article class="letterhead">
    <header class="brand">
      <span class="brand-dot"></span>
      <span class="brand-name">Cedar Hollow Family Medicine</span>
    </header>

    <section class="recipient">
      <div class="recipient-name">JOHN SMITH</div>
      <div>Street Name,City Name.</div>
      <div>Zip Coad 0000</div>
    </section>

    <div class="decor-bloom" role="img" aria-label="Faint dandelion seed-head decoration"></div>

    <section class="letter-body">
      <p>Lorem Ipsum is simply dummy text of the printing and typesetting industry. Lorem Ipsum has been the industry's standard dummy text ever since the 1500s, when an unknown printer took a galley of type and scrambled it to make a type specimen book. It has survived not only five centuries,but also the leap into electronic typesetting, remaining essentially unchanged. It was popularised in the 1960s with the release of Letraset sheets containing Lorem Ipsum passages, and more recently with desktop publishing software like Aldus PageMaker including versions of Lorem Ipsum.</p>
      <p>It is a long established fact that a reader will be distracted by the readable content of a page when looking at its layout. The point of using Lorem Ipsum is that it has a more-or-less normal distribution of letters, as opposed to using 'Content here, content here', making it look like readable English. Many desktop and web publishing packages and web page editors now use Lorem Ipsum as their default model text, and a search for 'lorem ipsum' will uncover many web sites still in their infancy. Various versions have evolved over the years, sometimes by accident, sometimes on purpose (injected humour and the like).</p>
    </section>

    <div class="signoff">Regards,</div>
    <div class="signature">John Doe</div>
    <div class="signer">
      <div>John Doe</div>
      <div class="signer-title">General Maneger</div>
    </div>

    <address class="contact" style="font-style: normal;">
      <div class="contact-company">Cedar Hollow Family Medicine, LLC</div>
      <div><strong>Salem:</strong> 971-555-0142 | <strong>Corvallis:</strong> 541-555-0187 | <strong>Fax:</strong> 503-555-0163</div>
      <div class="contact-email">info@cedarhollowmedicine.com</div>
    </address>

    <div class="footer-band"></div>
    <div class="footer-tab">www.cedarhollowmedicine.com</div>
  </article>
</main>
</body>
</html>
```